Business Card for innovative, tech/consultant company

We are specializing in bringing together Efficiency methodology and Technology for our Business customers. We would like an astonishing business Card that matches this idea.

Target Market(s)

Businesses of medium size or more

Industry/Entity Type

Business Consultant

Contact Information for Business Card

Name, Title, personal email, www, address, phone

Font styles to use
Sans Serif

Colors
3277b5

Requirements
Must have
• - innovative, efficient design
• - good readable
• - Colors must match our logo (blue and grey)
• - the attached font (is licensed by our Company) must be used (Syntax LT)
Should not have
• overloaded

```html
<!DOCTYPE html>
<html lang="en">
<head>
<meta charset="utf-8">
<title>Veritek Business Card</title>
<link rel="stylesheet" href="https://fonts.googleapis.com/css2?family=Cabin:wght@500&family=Arimo:wght@400&display=swap">
<style>
  :root {
    --page-bg: #1b1b1b;
    --brand-blue: #1f8bd0;
    --brand-blue-deep: #1a7fc2;
    --name-slate: #4c555c;
    --white: #ffffff;
    --photo-light: #e9ecee;
    --photo-mid: #c9ced2;
    --photo-dark: #3a444b;
  }
  * { margin: 0; padding: 0; box-sizing: border-box; }
  html, body {
    width: 1189px;
    height: 1200px;
    overflow: hidden;
    background: var(--page-bg);
  }
  .card {
    position: absolute;
    left: 94px;
    top: 315px;
    width: 1000px;
    height: 569px;
    display: flex;
    box-shadow: 0 10px 30px rgba(0,0,0,0.6);
  }
  .card__photo {
    position: relative;
    width: 515px;
    height: 100%;
    background: linear-gradient(180deg,
      var(--photo-mid) 0%,
      var(--photo-light) 22%,
      #f4f5f6 38%,
      #dfe3e6 55%,
      #6d7880 72%,
      var(--photo-dark) 100%);
    overflow: hidden;
  }
  .card__band {
    position: absolute;
    left: 0;
    top: 200px;
    width: 100%;
    height: 169px;
    background: rgba(255,255,255,0.35);
  }
  .card__company {
    position: absolute;
    left: 0;
    top: 200px;
    width: 100%;
    height: 169px;
    display: flex;
    align-items: center;
    justify-content: center;
    font-family: "Cabin", sans-serif;
    font-weight: 500;
    font-size: 64px;
    line-height: 1;
    color: var(--name-slate);
  }
  .card__info {
    flex: 1;
    height: 100%;
    background: linear-gradient(160deg, var(--brand-blue) 0%, var(--brand-blue-deep) 100%);
    position: relative;
    color: var(--white);
  }
  .card__name {
    position: absolute;
    left: 20px;
    top: 122px;
    font-family: "Cabin", sans-serif;
    font-weight: 500;
    font-size: 44px;
    line-height: 1;
  }
  .card__title {
    position: absolute;
    left: 20px;
    top: 168px;
    font-family: "Cabin", sans-serif;
    font-weight: 500;
    font-size: 33px;
    line-height: 1;
  }
  .contact-list {
    position: absolute;
    left: 22px;
    top: 333px;
    list-style: none;
  }
  .contact-list__item {
    display: flex;
    align-items: center;
    height: 34px;
    font-family: "Arimo", sans-serif;
    font-size: 28px;
    white-space: nowrap;
  }
  .contact-list__icon {
    width: 26px;
    height: 26px;
    margin-right: 32px;
    flex: none;
  }
</style>
</head>
<body>
  <div class="card">
    <div class="card__photo" role="img" aria-label="Photo of a bright, white modern office lobby with a glowing ceiling and dark glossy floor">
      <div class="card__band"></div>
      <div class="card__company">Veritek</div>
    </div>
    <div class="card__info">
      <h1 class="card__name">Clara Whitmore</h1>
      <p class="card__title">Managing Director</p>
      <ul class="contact-list">
        <li class="contact-list__item">
          <svg class="contact-list__icon" viewBox="0 0 26 26" aria-hidden="true">
            <rect width="26" height="26" rx="2" fill="#fff"/>
            <path d="M5 10 Q13 3 21 10 L19 12 L16 10 L10 10 L7 12 Z" fill="#1f8bd0"/>
            <rect x="7" y="12" width="12" height="9" rx="1.5" fill="#1f8bd0"/>
            <circle cx="13" cy="16.5" r="2.2" fill="#fff"/>
          </svg>
          031-5550-1824
        </li>
        <li class="contact-list__item">
          <svg class="contact-list__icon" viewBox="0 0 26 26" aria-hidden="true">
            <rect width="26" height="26" rx="2" fill="#fff"/>
            <circle cx="13" cy="13" r="9" fill="#1f8bd0"/>
            <ellipse cx="13" cy="13" rx="4" ry="9" fill="none" stroke="#fff" stroke-width="1.5"/>
            <line x1="4" y1="13" x2="22" y2="13" stroke="#fff" stroke-width="1.5"/>
          </svg>
          www.Veritek.com
        </li>
        <li class="contact-list__item">
          <svg class="contact-list__icon" viewBox="0 0 26 26" aria-hidden="true">
            <rect width="26" height="26" rx="2" fill="#fff"/>
            <rect x="4" y="7" width="18" height="12" fill="#1f8bd0"/>
            <path d="M4 7 L13 14 L22 7 M4 19 L10 13 M22 19 L16 13" fill="none" stroke="#fff" stroke-width="1.5"/>
          </svg>
          c.whitmore@veritek.com
        </li>
        <li class="contact-list__item">
          <svg class="contact-list__icon" viewBox="0 0 26 26" aria-hidden="true">
            <rect width="26" height="26" rx="2" fill="#fff"/>
            <path d="M13 22 C8 15 7 13 7 11 A6 6 0 0 1 19 11 C19 13 18 15 13 22 Z" fill="#1f8bd0"/>
            <circle cx="13" cy="11" r="2.3" fill="#fff"/>
          </svg>
          PO Box 482 Lindale 4107
        </li>
      </ul>
    </div>
  </div>
</body>
</html>
```